Life insurance company website and landing page

Web design is required for life insurance company. Specifically the company will 1) generate leads and 2) provide a blog. The target market of this business is people in their 50s and 60s, medium-high to high income earners, who are likely to have a policy in place already but want to save money on their premiums. Please read the attached design brief for more guidance. Open to any concepts that might work.The outputs for this job will include:1) a website2) a landing page3) fixing logos into a more useful and professional format (this should take 5 mins with the correct software)
Colors
Designer to choose colors to be used in the design.
Look and feel
Each slider illustrates characteristics of the customer's brand and the style your logo design should communicate.

```html
<!DOCTYPE html>
<html lang="en">
<head>
<meta charset="utf-8">
<title>CoverCompare.Life — Compare life insurance quotes</title>
<link href="https://fonts.googleapis.com/css2?family=Lato:wght@400;700;900&display=swap" rel="stylesheet">
<style>
:root{
  --red:#e31b23;
  --red-dark:#3b0a0e;
  --ink:#1f1f1f;
  --text:#4a4a4a;
  --grey-band:#efefef;
  --line:#d9d9d9;
  --white:#ffffff;
  --charcoal:#2b2b2b;
}
*{box-sizing:border-box;margin:0;padding:0}
html,body{width:1200px;height:4085px;overflow:hidden}
body{position:relative;background:var(--white);font-family:"Lato",sans-serif;color:var(--text)}
.abs{position:absolute}
.center{left:0;width:1200px;text-align:center}
.btn{position:absolute;left:478px;width:244px;height:50px;border-radius:5px;background:var(--red);color:var(--white);font:900 17px/50px "Lato",sans-serif;text-align:center;text-transform:uppercase;letter-spacing:.2px}

/* header */
.topline{top:0;left:0;width:1200px;height:4px;background:var(--red)}
.brand{top:50px;left:76px;display:flex;align-items:center;gap:12px;font:400 29px/1 "Lato",sans-serif;color:var(--ink)}
.brand-mark{width:26px;height:26px;border:4px solid var(--red);border-radius:6px}
.nav{top:62px;left:460px;display:flex;gap:0;font:700 14px/1 "Lato",sans-serif;color:var(--ink)}
.nav a{text-decoration:none;color:inherit;padding:0 21px;position:relative}
.nav a.active{color:var(--red)}
.nav a.active::after{content:"";position:absolute;left:12px;right:12px;top:26px;height:3px;background:var(--red)}

/* hero */
.hero-photo{top:127px;left:0;width:1200px;height:650px;background:linear-gradient(120deg,#a69a8e 0%,#cfc6bb 30%,#7b7a78 60%,#4c4c4e 100%)}
.hero-title{top:368px;font:900 47px/53px "Lato",sans-serif;color:var(--white);text-shadow:0 2px 6px rgba(0,0,0,.35)}
.dots{top:641px;left:558px;display:flex;gap:10px}
.dots span{width:13px;height:13px;border-radius:50%;background:var(--white)}
.dots span:first-child{background:var(--red)}

/* what we do */
.h2{font:900 34px/1 "Lato",sans-serif;color:var(--ink);text-transform:uppercase}
.sub-red{font:900 25px/1 "Lato",sans-serif;color:var(--red)}
.body-copy{font:400 16px/32px "Lato",sans-serif;color:var(--text)}

/* city band */
.city-photo{top:1141px;left:0;width:1200px;height:489px;background:linear-gradient(180deg,#2e2a33 0%,#4a3a3a 45%,#2f3540 75%,#232a33 100%)}
.city-title{top:1352px;font:900 35px/1 "Lato",sans-serif;color:var(--white)}
.city-text{top:1412px;font:400 17px/1 "Lato",sans-serif;color:var(--white)}

/* partners */
.partners{top:1790px;left:75px;width:1050px;display:grid;grid-template-columns:repeat(4,252px);grid-auto-rows:110px;gap:14px 14px}
.partner{border:2px solid var(--line);display:flex;align-items:center;justify-content:center;background:var(--white)}
.partner i{display:block;width:120px;height:44px;border-radius:8px;background:#d5d5d5}
.partner.offset{grid-column:2}

/* benefits */
.benefits-bg{top:2219px;left:0;width:1200px;height:580px;background:var(--grey-band)}
.benefit{top:2460px;width:330px;text-align:center}
.benefit .icon{width:114px;height:114px;border-radius:50%;background:var(--charcoal);margin:0 auto;display:flex;align-items:center;justify-content:center}
.benefit h3{margin-top:20px;font:900 24px/32px "Lato",sans-serif;color:var(--red)}
.benefit p{margin-top:4px;font:400 16px/27px "Lato",sans-serif;color:var(--text)}

/* blog */
.post{top:2923px;width:330px;text-align:center}
.post .thumb{height:197px}
.post .date{margin-top:24px;font:900 15px/1 "Lato",sans-serif;color:var(--ink);text-transform:uppercase}
.post h3{margin-top:17px;font:700 19px/29px "Lato",sans-serif;color:#333}
.post a{display:block;margin-top:14px;font:900 15px/1 "Lato",sans-serif;color:var(--red);text-decoration:none;text-transform:uppercase}

/* testimonials */
.testi-bg{top:3329px;left:0;width:1200px;height:450px;background:linear-gradient(100deg,var(--red-dark) 0%,#6e0d13 35%,#b3121b 70%,var(--red) 100%)}
.testi-title{top:3470px;font:900 34px/1 "Lato",sans-serif;color:var(--white);text-transform:uppercase}
.avatar{width:100px;height:100px;border-radius:50%;background:radial-gradient(circle at 40% 40%,#e8dccd,#a89580)}
.quote-badge{position:absolute;width:34px;height:34px;border-radius:50%;background:var(--red);border:3px solid var(--white)}
.quote{font:400 16px/28px "Lato",sans-serif;color:var(--white)}
.quote b{display:block;margin-top:14px;font-weight:700}

/* footer */
.footer-photo{top:3740px;left:0;width:1200px;height:345px;background:linear-gradient(160deg,#1e1416 0%,#2a1a1c 45%,#8e1118 80%,#c9151d 100%)}
.footer-name{top:3862px;font:400 26px/1 "Lato",sans-serif;color:var(--white)}
.footer-links{top:3944px;left:0;width:1200px;display:flex;justify-content:center;gap:40px;font:700 13px/1 "Lato",sans-serif;color:var(--white);text-transform:uppercase}
.copyright{top:3972px;font:400 12px/1 "Lato",sans-serif;color:#e6e6e6}
.social{top:4018px;left:507px;display:flex;gap:22px}
.social span{width:20px;height:20px;border-radius:50%;background:var(--white)}
</style>
</head>
<body>

<!-- header -->
<div class="abs topline"></div>
<div class="abs brand"><span class="brand-mark"></span>CoverCompare.Life</div>
<nav class="abs nav">
  <a class="active" href="#">Home</a><a href="#">What we do</a><a href="#">Benefits</a><a href="#">Blog</a><a href="#">Testimonials</a><a href="#">Contact</a>
</nav>

<!-- hero -->
<div class="abs hero-photo" role="img" aria-label="Photo of a smiling couple in their sixties looking at a laptop at home"></div>
<svg class="abs" style="top:677px;left:0" width="1200" height="101" viewBox="0 0 1200 101" aria-hidden="true">
  <path d="M0 25 C90 55 200 100 300 100 C450 100 560 30 720 5 C790 -5 820 100 860 100 C960 100 1080 40 1200 20 L1200 101 L0 101 Z" fill="#fff"/>
</svg>
<h1 class="abs center hero-title">Compare quotes from Australia's leading<br>life insurers for free today</h1>
<a class="btn" style="top:501px">Get free quotes now</a>
<div class="abs dots"><span></span><span></span><span></span><span></span></div>

<!-- what we do -->
<h2 class="abs center h2" style="top:840px">What we do</h2>
<p class="abs center sub-red" style="top:899px">Compare Australia's leading life insurers, free</p>
<p class="abs center body-copy" style="top:932px">CoverCompare.Life helps you find the most appropriate and cost effective options by comparing a variety of<br>leading insurers at the same time.</p>
<a class="btn" style="top:1039px">Get free quotes now</a>

<!-- city band -->
<div class="abs city-photo" role="img" aria-label="Evening photo of a harbour city skyline with an opera house on the water"></div>
<svg class="abs" style="top:1140px;left:0" width="1200" height="90" viewBox="0 0 1200 90" aria-hidden="true">
  <path d="M0 0 L1200 0 L1200 80 C1120 40 1020 10 940 30 C860 50 820 90 740 80 C620 60 560 0 470 15 C380 30 320 80 240 75 C170 70 110 10 60 20 C30 25 10 40 0 50 Z" fill="#fff"/>
</svg>
<h2 class="abs center city-title">Home of everything life insurance in Australia</h2>
<p class="abs center city-text">Everything you need to know about life insurance and income protection in Australia.</p>
<a class="btn" style="top:1467px">Stay informed</a>

<!-- partners -->
<h2 class="abs center h2" style="top:1680px">Our partners</h2>
<p class="abs center" style="top:1740px;font:400 16px/1 'Lato',sans-serif">Australia's leading insurers, we can help you compare them</p>
<div class="abs partners">
  <div class="partner" aria-label="Partner insurer"><i></i></div>
  <div class="partner" aria-label="Partner insurer"><i></i></div>
  <div class="partner" aria-label="Partner insurer"><i></i></div>
  <div class="partner" aria-label="Partner insurer"><i></i></div>
  <div class="partner" aria-label="Partner insurer"><i></i></div>
  <div class="partner" aria-label="Partner insurer"><i></i></div>
  <div class="partner" aria-label="Partner insurer"><i></i></div>
  <div class="partner" aria-label="Partner insurer"><i></i></div>
  <div class="partner offset" aria-label="Partner insurer"><i></i></div>
  <div class="partner" aria-label="Partner insurer"><i></i></div>
</div>

<!-- benefits -->
<svg class="abs" style="top:2219px;left:0" width="1200" height="90" viewBox="0 0 1200 90" aria-hidden="true">
  <rect width="1200" height="90" fill="#efefef"/>
  <path d="M0 0 L1200 0 L1200 75 C1130 40 1050 0 980 5 C900 10 860 60 780 60 C680 60 560 0 480 5 C400 10 350 60 260 55 C170 50 80 0 0 15 Z" fill="#fff"/>
</svg>
<div class="abs benefits-bg" style="top:2309px;height:490px"></div>
<h2 class="abs center h2" style="top:2382px">Benefits</h2>

<div class="abs benefit" style="left:74px">
  <div class="icon"><svg width="54" height="40" viewBox="0 0 54 40" fill="none" stroke="#fff" stroke-width="4"><path d="M2 2 V38 H52"/><path d="M10 30 L22 18 L30 24 L46 8"/><path d="M38 8 H46 V16"/></svg></div>
  <h3>Need a high level of cover<br>at a low price?</h3>
  <p>Our highly experienced brokers can help<br>you compare 11 of Australia's leading<br>insurers simultaneously.</p>
</div>
<div class="abs benefit" style="left:435px">
  <div class="icon"><svg width="36" height="46" viewBox="0 0 36 46"><path d="M2 2 H24 L34 12 V44 H2 Z" fill="#fff"/><path d="M9 22 H27 M9 29 H27 M9 36 H27" stroke="#2b2b2b" stroke-width="3"/></svg></div>
  <h3>No hidden fees</h3>
  <p>Pay the same as going direct to the<br>insurer, or even less</p>
</div>
<div class="abs benefit" style="left:794px">
  <div class="icon"><svg width="54" height="38" viewBox="0 0 54 38" fill="none" stroke="#fff" stroke-width="4"><rect x="8" y="3" width="38" height="24" rx="2"/><path d="M2 34 H52"/></svg></div>
  <h3>Learn how<br>life insurance works</h3>
  <p>For articles, videos, guides, and<br>anything else life insurance related,<br>visit our blog</p>
</div>

<!-- blog -->
<h2 class="abs center h2" style="top:2852px">Blog posts</h2>
<article class="abs post" style="left:75px">
  <div class="thumb" role="img" aria-label="Photo of hands cupped around a red paper heart and family cut-out" style="background:linear-gradient(135deg,#f1eeee,#d8d2d4 60%,#c43a3f)"></div>
  <p class="date">September 19, 2019</p>
  <h3>Aenean vulputate enim et augue<br>posuere accumsan.</h3>
  <a href="#">Learn more</a>
</article>
<article class="abs post" style="left:436px">
  <div class="thumb" role="img" aria-label="Photo of an older couple meeting with an adviser at a desk" style="background:linear-gradient(135deg,#5d6066,#a9a6a1 50%,#e2ddd6)"></div>
  <p class="date">September 19, 2019</p>
  <h3>Aenean vulputate enim et augue<br>posuere accumsan.</h3>
  <a href="#">Learn more</a>
</article>
<article class="abs post" style="left:796px">
  <div class="thumb" role="img" aria-label="Photo of an insurance form and pen on a wooden desk" style="background:linear-gradient(135deg,#2c221c,#6b5849 45%,#d9cfc2)"></div>
  <p class="date">September 19, 2019</p>
  <h3>Aenean vulputate enim et augue<br>posuere accumsan.</h3>
  <a href="#">Learn more</a>
</article>

<!-- testimonials -->
<div class="abs testi-bg"></div>
<svg class="abs" style="top:3329px;left:0" width="1200" height="90" viewBox="0 0 1200 90" aria-hidden="true">
  <path d="M0 0 L1200 0 L1200 40 C1100 0 1000 -5 900 20 C820 40 780 80 680 70 C560 60 500 5 380 10 C260 15 200 60 100 50 C50 45 20 25 0 15 Z" fill="#fff"/>
</svg>
<h2 class="abs center testi-title">Testimonials</h2>

<div class="abs avatar" style="top:3543px;left:75px" role="img" aria-label="Portrait photo of a customer"></div>
<span class="quote-badge" style="top:3614px;left:137px"></span>
<p class="abs quote" style="top:3533px;left:197px;width:380px">“ Aenean mollis, sem scelerisque rhoncus mollis, eros augue consectetur nisl, vestibulum blandit quam lacus et dui sit amet ultricies tortor, eget facilisis..”<b>- Rosalind</b></p>

<div class="abs avatar" style="top:3543px;left:615px" role="img" aria-label="Portrait photo of a customer"></div>
<span class="quote-badge" style="top:3614px;left:677px"></span>
<p class="abs quote" style="top:3533px;left:737px;width:380px">“ Aenean mollis, sem scelerisque rhoncus mollis, eros augue consectetur nisl, vestibulum blandit quam lacus et dui sit amet ultricies tortor, eget facilisis..”<b>- Graham</b></p>

<!-- footer -->
<div class="abs footer-photo" role="img" aria-label="Silhouette photo of a parent lifting a child against a red sunset sky"></div>
<p class="abs center footer-name">CoverCompare.Life</p>
<div class="abs footer-links"><span>Terms of use</span><span>Contact us</span><span>Privacy policy</span></div>
<p class="abs center copyright">Copyright © 2019 Company Name All Rights Reserved</p>
<div class="abs social" aria-label="Social links"><span></span><span></span><span></span><span></span><span></span></div>

</body>
</html>
```